vellar.com music website

I need a graphic designer to help me design a very modern looking theme for vellar.com, a website for sharing songs. I currently have a very ugly old-looking design that I want to replace. I need a great logo, a great page theme. Just one comp is all I need of the home page. Must have two tag lines: "it pays to share" and "get paid to share music" The current design has all the elements I need, so I have attached it as a download. vellar is pronounced vehlar. the current site is not live. Please feel free to send me questions.
Updates

Reason: I want to give everyone a chance to get their design in. Thank you.

Target Market(s)

The site needs to appeal to music fans that will be pulled in by the concept of "it pays to share," as well as the pop of the design. It has to look fun and cool. Empahsis on modern looking design.

Industry/Entity Type

Graphic Designer

Requirements
Must have
• engaging logo, there must be a container that holds video, scrolls right and left. 6 action buttons, for Plumora, Zendrol, My, Add, Search, More. You can put the first letter only on the buttons. Must have two tag lines: "it pays to share" and "get paid to share music" Please include the elements, such as login, join, etc... that are in the comp that you can download. Obviously I don't want it to look like what I already have, except that it must have a container that holds the video. The container that holds the video has to have the same aspect ratio that kobrastream uses for it's embed codes. You can find this ratio by checking any kobrastream video embed code, they have a custom size tool which lets you play with the sizes. Any question, pls contact thanks.
Nice to have
• unlike the existing comp, it can have white space. Just looking for a good modern theme with a cool logo. Jquery style themes might be nice... Also, think along the lines of a cool techy feel for mobile...

This is a cool image, but obviously don't get too close to it because it belongs to another music site:

http://kpnoverbyte2011.files.brindlehost.com/2012/03/capture-2012-03-28-at-12-02-36-pm.png?w=194

```html
<!DOCTYPE html>
<html lang="en">
<head>
<meta charset="utf-8">
<title>vellar – it pays to share</title>
<link href="https://fonts.googleapis.com/css2?family=Poppins:wght@400;500;600&display=swap" rel="stylesheet">
<style>
  :root{
    --bg:#f4f6fb;
    --ink:#1c1f2b;
    --muted:#6b7184;
    --line:#e2e6ef;
    --card:#ffffff;
    --accent:#ff3d7f;
    --accent-2:#7b5cff;
    --band-a:#14162b;
    --band-b:#3b2a7a;
    --video-a:#2b3350;
    --video-b:#7a5a3a;
    --btn-plumora:#3b5bdb;
    --btn-zendrol:#1ca3e0;
    --btn-my:#7b5cff;
    --btn-add:#ff3d7f;
    --btn-search:#14b8a6;
    --btn-more:#8a90a3;
  }
  *{box-sizing:border-box;margin:0;padding:0}
  html,body{width:1156px;height:1200px;overflow:hidden}
  body{position:relative;background:var(--bg);color:var(--ink);font-family:"Poppins",sans-serif}

  .topbar{position:absolute;left:0;top:0;width:1156px;height:88px;padding:0 64px;display:flex;align-items:center;background:var(--card);border-bottom:1px solid var(--line)}
  .brand{display:flex;align-items:center;gap:12px}
  .brand-dot{width:34px;height:34px;border-radius:50%;background:var(--accent)}
  .brand-name{font-size:32px;font-weight:600;color:var(--ink);line-height:1}
  .tagline{margin-left:28px;padding-left:28px;border-left:1px solid var(--line);font-size:18px;color:var(--muted)}
  .account{margin-left:auto;display:flex;align-items:center;gap:18px;font-size:16px}
  .donate{font-size:13px;font-weight:500;color:var(--ink);background:#ffe45c;padding:6px 14px;border-radius:20px}
  .login{color:var(--ink)}
  .join{color:#fff;background:var(--accent);padding:9px 24px;border-radius:22px;font-weight:500}

  .band{position:absolute;left:0;top:88px;width:1156px;height:300px;background:linear-gradient(120deg,var(--band-a),var(--band-b))}

  .player{position:absolute;left:128px;top:120px;width:900px;height:562px;background:var(--card);border-radius:18px;box-shadow:0 20px 50px rgba(20,22,43,.18)}
  .player-head,.player-foot{position:absolute;left:50px;width:800px;height:56px;display:flex;align-items:center;justify-content:space-between}
  .player-head{top:0}
  .player-foot{top:506px}
  .song{font-size:22px;font-weight:600}
  .count{font-size:15px;color:var(--accent);font-weight:500}
  .artist{font-size:18px;font-weight:500}
  .follow{font-size:15px;color:var(--accent-2);font-weight:500}
  .video{position:absolute;left:50px;top:56px;width:800px;height:450px;border-radius:10px;background:linear-gradient(110deg,var(--video-a) 0,#242a40 50%,var(--video-b) 100%)}
  .play{position:absolute;left:360px;top:185px;width:80px;height:80px}
  .nav-arrow{position:absolute;top:259px;width:40px;height:40px}
  .nav-arrow.prev{left:5px}
  .nav-arrow.next{right:5px}

  .actions{position:absolute;top:720px;left:0;width:1156px;display:flex;justify-content:center;gap:28px;list-style:none}
  .actions li{width:84px;display:flex;flex-direction:column;align-items:center;gap:8px;font-size:14px;color:var(--muted)}
  .actions .key{width:60px;height:60px;border-radius:50%;display:flex;align-items:center;justify-content:center;color:#fff;font-size:24px;font-weight:600}
  .k-plumora{background:var(--btn-plumora)}.k-zendrol{background:var(--btn-zendrol)}.k-my{background:var(--btn-my)}
  .k-add{background:var(--btn-add)}.k-search{background:var(--btn-search)}.k-more{background:var(--btn-more)}

  .slogan{position:absolute;top:860px;left:0;width:1156px;text-align:center;font-size:38px;font-weight:600;color:var(--ink)}
  .slogan em{font-style:normal;color:var(--accent)}

  .footer{position:absolute;left:64px;top:1000px;width:1028px;border-top:1px solid var(--line);padding-top:34px}
  .footer-nav{display:flex;justify-content:center;gap:36px;font-size:15px;color:var(--ink)}
  .legal{margin-top:26px;text-align:center;font-size:13px;color:var(--muted)}
</style>
</head>
<body>
  <header class="topbar">
    <div class="brand">
      <div class="brand-dot"></div>
      <div class="brand-name">vellar</div>
    </div>
    <div class="tagline">it pays to share</div>
    <nav class="account">
      <span class="donate">Donate to St. Brennan</span>
      <span class="login">Login</span>
      <span class="join">Join</span>
    </nav>
  </header>

  <div class="band"></div>

  <section class="player">
    <div class="player-head">
      <span class="song">Vampire Love</span>
      <span class="count">1,234 fans</span>
    </div>
    <svg class="nav-arrow prev" viewBox="0 0 40 40" aria-hidden="true">
      <circle cx="20" cy="20" r="19" fill="#f4f6fb" stroke="#e2e6ef"/><path d="M23 13 L16 20 L23 27" fill="none" stroke="#1c1f2b" stroke-width="2.5"/>
    </svg>
    <div class="video" role="img" aria-label="Video of a folk band performing on stage with singers and brass players">
      <svg class="play" viewBox="0 0 80 80" aria-hidden="true">
        <circle cx="40" cy="40" r="38" fill="rgba(255,255,255,.9)"/><path d="M33 26 L55 40 L33 54Z" fill="#ff3d7f"/>
      </svg>
    </div>
    <svg class="nav-arrow next" viewBox="0 0 40 40" aria-hidden="true">
      <circle cx="20" cy="20" r="19" fill="#f4f6fb" stroke="#e2e6ef"/><path d="M17 13 L24 20 L17 27" fill="none" stroke="#1c1f2b" stroke-width="2.5"/>
    </svg>
    <div class="player-foot">
      <span class="follow">+ Follow</span>
      <span class="artist">Morvelka</span>
      <span class="count">10,456 vellars</span>
    </div>
  </section>

  <ul class="actions">
    <li><span class="key k-plumora">P</span>Plumora</li>
    <li><span class="key k-zendrol">Z</span>Zendrol</li>
    <li><span class="key k-my">M</span>My</li>
    <li><span class="key k-add">A</span>Add</li>
    <li><span class="key k-search">S</span>Search</li>
    <li><span class="key k-more">M</span>More</li>
  </ul>

  <p class="slogan">get paid to <em>share music</em></p>

  <footer class="footer">
    <nav class="footer-nav">
      <span>Home</span><span>About</span><span>Terms</span><span>Privacy</span><span>Settings</span><span>Support</span>
    </nav>
    <p class="legal">© 2012 Kindred Share Meida US patent pending 1,352,874</p>
  </footer>
</body>
</html>
```